Marrowgate Bidding Consortium
Auctioneers & Appraiser
Marrowgate Bidding Consortium - Antiques and Collectibles
Creative Brief
Antiques and Collectibles
www.marrowBids.example
Marrowgate Bidding Consortium sales specialists provide expertise and detailed understanding of the current markets along with professional accuracy and advice to our clients. In addition, Holloway's Trusts & Estates department offers various services to facilitate any full estate sale, and a willingness to work at the client's discretion. The auction house's has allowed MBC's to expand into the China market. This alliance has enhanced MBC's capability to maximize the sale potential in an international market, while maintaining the company's unique standard of one-on-one client service. Today, the Auction house is furthering their growth with a greater concentration in specialized departments. As a leading regional auction house, MBC's is progressing forward with the expanding global market, and is looking to the future to provide services which MBC's clients require and deserve
below header
http://www.vendrelhall.example/
http://oddlotgoods.example/
http://www.hollowaysbids.example/

```html
<!DOCTYPE html>
<html lang="en">
<head>
<meta charset="utf-8">
<title>Marrowgate Bidding Consortium – Auctioneers &amp; Appraisers</title>
<link href="https://fonts.googleapis.com/css2?family=Arimo:wght@400;700&display=swap" rel="stylesheet">
<style>
:root{
  --red:#b8291c;
  --red-dark:#8e1d12;
  --orange:#d9782a;
  --ink:#222;
  --muted:#555;
  --bar:#111;
  --page:#e9e9e9;
  --panel:#fff;
  --line:#d6d6d6;
  --footer:#2e2e2e;
  --footer-text:#cfcfcf;
}
*{box-sizing:border-box;margin:0;padding:0}
html,body{width:1200px;height:904px;overflow:hidden}
body{position:relative;font-family:"Arimo",Arial,sans-serif;color:var(--ink);
  background:linear-gradient(#f6f6f6,#e4e4e4 170px,var(--page) 170px);}
.abs{position:absolute}

/* header */
.account-tab{left:828px;top:0;width:300px;height:24px;background:var(--red);color:#fff;
  font-size:12px;font-weight:700;display:flex;align-items:center;justify-content:center;gap:18px}
.brand{left:420px;top:34px;width:360px;display:flex;flex-direction:column;align-items:center;gap:10px}
.brand-mark{width:44px;height:44px;background:var(--red)}
.brand-name{font-size:20px;font-weight:700;color:var(--red);text-align:center;line-height:1.15;letter-spacing:.5px}
.search{left:828px;top:108px;width:228px;height:36px;background:#fff;border:1px solid #bbb;border-radius:3px;
  display:flex;align-items:center;padding:0 10px;font-size:13px;color:#999;justify-content:space-between}

/* nav */
.main-nav{left:0;top:168px;width:1200px;height:36px;background:linear-gradient(#2a2a2a,var(--bar))}
.nav-item{position:absolute;top:168px;height:36px;line-height:36px;color:#fff;font-size:15px;text-align:center}
.nav-item.active{background:linear-gradient(var(--red),var(--red-dark));height:36px}
.nav-sep{position:absolute;top:176px;width:1px;height:20px;background:#444}

/* content */
.sheet{left:125px;top:221px;width:924px;height:559px;background:#f1f1f1;box-shadow:0 0 8px rgba(0,0,0,.35)}
.panel{position:absolute;background:var(--panel);border:1px solid var(--line)}
.panel-title{font-size:16px;text-align:center;padding:10px 0 8px;border-bottom:2px solid var(--red);margin:0 8px}
.row{display:flex;justify-content:space-between;font-size:11px;padding:0 10px}
.days{display:flex;align-items:flex-end;gap:4px;padding:10px 10px 0}
.days b{font-size:58px;color:var(--red);line-height:.9}
.days span{font-size:14px;color:var(--muted)}
.timer{color:var(--red)}
.register{text-decoration:underline;color:var(--ink)}
.schedule{padding:6px 10px}
.schedule h4{font-size:11px;color:var(--red);margin:8px 0 6px}
.schedule h4.first{color:var(--orange)}
.schedule p{display:flex;justify-content:space-between;font-size:11px;padding:5px 0;border-bottom:1px solid #e5e5e5}
.bid-banner{left:137px;top:629px;width:206px;height:96px;background:linear-gradient(#5a3418,#2a160a);
  display:flex;flex-direction:column;justify-content:flex-end;align-items:center;color:#fff;font-size:12px;font-weight:700;padding-bottom:8px;line-height:1.3}
.feature-sub{font-size:12px;color:var(--red);text-align:center;margin-top:8px}
.feature-img{position:absolute;left:10px;top:70px;width:417px;height:372px;
  background:linear-gradient(160deg,#2e4a6a,#6d7f8c 45%,#c9c3b2 75%,#8fa3b5)}
.dots{position:absolute;right:20px;bottom:14px;display:flex;gap:5px}
.dots i{width:9px;height:9px;border-radius:50%;background:#fff;opacity:.8}
.dots i:first-child{background:#444}
.follow{display:flex;align-items:center;justify-content:center;gap:10px;height:100%;font-size:16px}
.follow span{margin-right:18px}
.follow i{width:24px;height:24px;background:#9a9a9a;border-radius:3px}
.news{padding:8px 8px 0;border-bottom:1px solid #e5e5e5;height:144px}
.news-date{font-size:11px}
.news-head{font-size:11px;color:var(--red);margin:4px 0 6px}
.news-body{display:flex;gap:8px}
.news-thumb{width:78px;height:58px;flex:none}
.news-text{font-size:11px;line-height:1.35;color:#333}
.more{font-size:11px;color:var(--orange);text-align:right;margin-top:8px}

/* footer */
.site-footer{left:0;top:763px;width:1200px;height:141px;background:var(--footer)}
.footer-nav{left:137px;top:798px;font-size:13px;color:var(--footer-text);word-spacing:2px}
.copyright{left:137px;top:840px;font-size:12px;color:var(--footer-text)}
.footer-brand{left:900px;top:790px;width:150px;display:flex;flex-direction:column;align-items:center;gap:6px}
.footer-brand i{width:26px;height:26px;background:#777}
.footer-brand b{font-size:12px;color:#9a9a9a;text-align:center;line-height:1.2}
</style>
</head>
<body>

<header>
  <div class="abs account-tab"><span>Live Auction Sign In</span><span>|</span><span>Register</span></div>
  <div class="abs brand">
    <div class="brand-mark"></div>
    <div class="brand-name">MARROWGATE<br>BIDDING CONSORTIUM</div>
  </div>
  <div class="abs search"><span>Search</span>
    <svg width="16" height="16" viewBox="0 0 16 16"><circle cx="6.5" cy="6.5" r="5" fill="none" stroke="#555" stroke-width="2"/><line x1="10" y1="10" x2="15" y2="15" stroke="#555" stroke-width="2.4"/></svg>
  </div>
</header>

<nav>
  <div class="abs main-nav"></div>
  <a class="nav-item active" style="left:127px;width:89px">Home</a>
  <a class="nav-item" style="left:222px;width:100px">Next Auction</a>
  <a class="nav-item" style="left:350px;width:140px">Previous Auctions</a>
  <a class="nav-item" style="left:505px;width:65px">News</a>
  <a class="nav-item" style="left:585px;width:80px">Catalogs</a>
  <a class="nav-item" style="left:685px;width:70px">Results</a>
  <a class="nav-item" style="left:775px;width:70px">Buying</a>
  <a class="nav-item" style="left:865px;width:70px">Selling</a>
  <a class="nav-item" style="left:955px;width:80px">Contact</a>
  <span class="nav-sep" style="left:336px"></span><span class="nav-sep" style="left:498px"></span>
  <span class="nav-sep" style="left:578px"></span><span class="nav-sep" style="left:675px"></span>
  <span class="nav-sep" style="left:765px"></span><span class="nav-sep" style="left:855px"></span>
  <span class="nav-sep" style="left:945px"></span>
</nav>

<footer>
  <div class="abs site-footer"></div>
  <div class="abs footer-nav">Home &nbsp;| Next Auction &nbsp;| Previous Auctions &nbsp;| News &nbsp;| Catalogs &nbsp;| Results &nbsp;| Buying &nbsp;| Selling &nbsp;| Contact</div>
  <div class="abs copyright">© 2013 marrowBids &nbsp;| All Rights Reserved. &nbsp;&nbsp;Privacy Policy Legal Information Terms &amp; Conditions</div>
  <div class="abs footer-brand"><i></i><b>MARROWGATE<br>BIDDING CONSORTIUM</b></div>
</footer>

<main>
  <div class="abs sheet"></div>

  <section class="panel" style="left:137px;top:226px;width:218px;height:150px">
    <h2 class="panel-title">NEXT AUCTION</h2>
    <div class="row" style="margin-top:10px"><span>August 10, 2013</span><span>12:00pm</span></div>
    <div class="days"><b>5</b><span>Days</span></div>
    <div class="row" style="margin-top:8px"><span class="timer">10 hr 00 min 45 sec</span><span class="register">REGISTER NOW</span></div>
  </section>

  <section class="panel schedule" style="left:137px;top:382px;width:218px;height:240px">
    <h4 class="first">Auction Preview</h4>
    <p><span>August 5, 2013</span><span>11 - 6pm</span></p>
    <p><span>August 6, 2013</span><span>11 - 6pm</span></p>
    <p><span>August 7, 2013</span><span>11 - 6pm</span></p>
    <h4>Welcome Reception</h4>
    <p><span>August 5, 2013</span><span>10 - 6pm</span></p>
    <h4>Live Online Bidding</h4>
    <p><span>August 20, 2013</span><span>10- 6pm</span></p>
  </section>

  <div class="abs bid-banner" role="img" aria-label="Photo of an auction room interior with bid order caption">BID ORDER<br>TELEPHONE/ABSENTEE</div>

  <section class="panel" style="left:365px;top:226px;width:439px;height:450px">
    <h2 class="panel-title" style="border-bottom:none;padding-bottom:0">AUGUST 20, 2013 - MARROWGATE ARTS ANTIQUES</h2>
    <p class="feature-sub">August 20, 2013 · Marrowgate Glass &amp; Glassware</p>
    <div class="feature-img" role="img" aria-label="Photo of porcelain vases, figurines and glassware displayed on a table">
      <div class="dots"><i></i><i></i><i></i></div>
    </div>
  </section>

  <section class="panel" style="left:365px;top:684px;width:439px;height:53px">
    <div class="follow"><span>Follow Us</span><i></i><i></i><i></i><i></i><i></i></div>
  </section>

  <section class="panel" style="left:816px;top:226px;width:223px;height:512px">
    <h2 class="panel-title">LATEST NEWS</h2>
    <article class="news">
      <div class="news-date">August 5, 2013</div>
      <div class="news-head">Lorem ipsum dolor sit amectetu</div>
      <div class="news-body"><div class="news-thumb" role="img" aria-label="Photo of antique ceramics" style="background:linear-gradient(#6a7f95,#c2b49a)"></div>
        <div class="news-text">Lorem ipsum dolor sit amet, consect ahet adipiscing elit, sed diam nonummy</div></div>
      <div class="more">Read More »</div>
    </article>
    <article class="news">
      <div class="news-date">August 5, 2013</div>
      <div class="news-head">Lorem ipsum dolor sit amectetu</div>
      <div class="news-body"><div class="news-thumb" role="img" aria-label="Photo of an auction sale display" style="background:linear-gradient(#8a3a3a,#d0a070)"></div>
        <div class="news-text">Lorem ipsum dolor sit amet, consect ahet adipiscing elit, sed diam nonummy</div></div>
      <div class="more">Read More »</div>
    </article>
    <article class="news" style="border-bottom:none">
      <div class="news-date">August 5, 2013</div>
      <div class="news-head">Lorem ipsum dolor sit amectetu</div>
      <div class="news-body"><div class="news-thumb" role="img" aria-label="Photo of collectible objects" style="background:linear-gradient(#5a3a5a,#c27a6a)"></div>
        <div class="news-text">Lorem ipsum dolor sit amet, consect ahet adipiscing elit, sed diam nonummy</div></div>
      <div class="more">Read More »</div>
    </article>
  </section>
</main>

</body>
</html>
```